Corvane Partners Web Design

Dear all
I need a web design for a financial services site. We are a broker who deals with many different financial institutions and require a clean, simple and instantly impressive site based on the colour scheme that SketchGuild created for us. A landing page (www.crvnp.mx) gives an idea of the logo and clour scheme but we are looking at either a one page site with rollover text boxes or a 3 or 4 page site depending on the preference of the designer and the best user experience. The site“s purpose is to give confidence that the company exists rather than impart pages of information although we would like this to be a site that can expand over time as the company grows. For now the requirement is for a clear set of possibly changing images at the centre of a white screen that relate to finance in general nad the benefits of wealth creation as well as sectios either along the top or bottom - Our Company, Our Approach, Our services, Our clients, Contact (user to fill in contact box to be sent to info@crvnp.mx. The text for each of these boxes I assume can be added by the coding team here, it the overall look and feel that I am looking for from SketchGuild - deadline can be extended if necessary but I was hoping to wrap this all up in October

Target Market(s)

Succesful individuals looking to maximise returns on their investment via world class financial institutions and supported throughout by qualified independent financial advisors

Industry/Entity Type

Finance

Requirements
Must have
• Logo and color scheme of the logo design SketchGuild sent - I have all these sourcefiles, pantone and fonts

```html
<!DOCTYPE html>
<html lang="en">
<head>
<meta charset="utf-8">
<title>Corvane Partners</title>
<link href="https://fonts.googleapis.com/css2?family=Open+Sans:wght@300;400;600;700&display=swap" rel="stylesheet">
<style>
:root{
  --navy:#1c2e52;
  --navy-dark:#14223f;
  --heading:#2c3b5c;
  --body-text:#4a4f57;
  --page-bg:#f7f9f9;
  --rule:#b9bcbf;
  --accent:#f2a21c;
  --footer-bg:#878e91;
  --field:#c9c9c9;
  --white:#ffffff;
}
*{margin:0;padding:0;box-sizing:border-box}
html,body{width:1108px;height:1200px;overflow:hidden;background:var(--white)}
body{font-family:'Open Sans',Arial,sans-serif;color:var(--body-text)}
.stage{position:absolute;left:0;top:0;width:1200px;height:1300px;transform:scale(0.92333);transform-origin:0 0}
.page{position:absolute;left:310px;top:0;width:581px;height:1300px;background:var(--white)}
.abs{position:absolute}

/* header */
.header{left:0;top:0;width:581px;height:73px;background:#f8fafa;border-top:3px solid var(--navy)}
.call-tab{left:322px;top:-3px;width:196px;height:23px}
.call-text{left:356px;top:5px;font-size:7.5px;color:var(--white);font-weight:600;white-space:nowrap}
.call-text b{color:var(--accent)}
.brand{left:66px;top:28px;text-align:center;width:90px}
.brand-mark{width:14px;height:14px;background:var(--navy);margin:0 auto 6px;border-radius:50%}
.brand-name{font-size:11px;letter-spacing:6px;color:var(--navy);font-weight:400}
.nav{left:214px;top:41px;display:flex;gap:0}
.nav a{font-size:8.5px;font-weight:700;color:var(--navy);text-decoration:none;position:absolute;white-space:nowrap}

/* hero */
.hero{left:0;top:73px;width:581px;height:305px;background:linear-gradient(100deg,#6b5338 0%,#a88254 30%,#5a4632 55%,#2b2522 80%,#4a4036 100%)}
.hero-title{left:64px;top:73px;font-size:23.5px;font-weight:300;color:var(--white);line-height:27px}
.hero-sub{left:64px;top:143px;font-size:8.5px;font-weight:700;color:var(--white)}
.btn{background:linear-gradient(#3a4f78,var(--navy-dark));color:var(--white);font-size:8.5px;font-weight:700;text-align:center;border-radius:2px;box-shadow:0 1px 2px rgba(0,0,0,.4)}
.hero-btn{left:65px;top:174px;width:92px;height:26px;line-height:26px}
.hero-link{left:169px;top:181px;font-size:8.5px;font-weight:700;color:var(--white);text-decoration:underline}

/* sections */
.content{left:0;top:378px;width:581px;height:589px;background:var(--page-bg)}
.section-title{font-size:14.5px;font-weight:400;color:var(--heading)}
.copy{font-size:7.6px;line-height:11.6px;color:var(--body-text);width:252px}
.copy p+p{margin-top:11.6px}
.photo{background:linear-gradient(135deg,#e9ebee,#c9cdd3 60%,#8d8f96)}
.rule{height:1px;background:var(--rule);left:59px;width:465px}

/* clients */
.clients-title{left:0;width:581px;top:991px;text-align:center;font-size:14px;font-weight:300;color:#8b8f94}
.client{top:1028px;font-size:11px;font-weight:600;color:#6a6d72;display:flex;align-items:center;gap:4px;white-space:nowrap}
.client i{display:inline-block;width:7px;height:7px;border-radius:50%;background:#6a6d72}

/* contact */
.contact{left:0;top:1067px;width:581px;height:233px;background:var(--footer-bg)}
.contact-title{left:63px;top:23px;font-size:14.5px;font-weight:300;color:var(--white)}
.contact-note{left:63px;top:48px;font-size:5.5px;color:var(--white)}
.field{background:var(--field);border:1px solid #b5b5b5;font-size:5.5px;color:#7b7f82;padding:5px 6px}
.details{font-size:5.5px;line-height:11px;color:var(--white);font-weight:600}
.map{left:295px;top:65px;width:228px;height:93px;background:linear-gradient(120deg,#e8e6e1,#dcdad3 50%,#efe7b8)}
.enquire{left:63px;top:171px;width:86px;height:20px;line-height:20px;font-size:8px}
.footer-rule{left:59px;top:216px;width:465px;height:1px;background:#9ba1a4}
.copyright{left:0;width:581px;top:220px;text-align:center;font-size:5.5px;color:#3d4246}
</style>
</head>
<body>
<div class="stage">
<div class="page">

  <header class="abs header">
    <svg class="abs call-tab" viewBox="0 0 196 23" aria-hidden="true"><polygon points="0,0 196,0 188,23 8,23" fill="#1c2e52"/></svg>
    <svg class="abs" style="left:336px;top:4px" width="11" height="11" viewBox="0 0 11 11" aria-hidden="true"><circle cx="5.5" cy="5.5" r="4.8" fill="none" stroke="#9aa6bf" stroke-width=".8"/><path d="M3.6 3.2l1 1-.5.7c.3.7.8 1.2 1.5 1.5l.7-.5 1 1-.7.8C5 7.6 3.4 6 3 4z" fill="#9aa6bf"/></svg>
    <div class="abs call-text">FOR INQUIRIES, CALL US: <b>(02) 5550 0192</b></div>
    <div class="abs brand"><div class="brand-mark"></div><div class="brand-name">CORVANE</div></div>
    <nav class="abs nav">
      <a style="left:0">About Us</a>
      <a style="left:63px">Our Approach</a>
      <a style="left:146px">Services</a>
      <a style="left:204px">Clients</a>
      <a style="left:257px">Contact Us</a>
    </nav>
  </header>

  <section class="abs hero" role="img" aria-label="Portrait photo of a smiling businessman in a dark jacket, blurred warm office background">
    <h1 class="abs hero-title">Designing investment<br>solutions for clients.</h1>
    <p class="abs hero-sub">Lorem ipsum dolor sit amet, consectetur adipisicing elit,</p>
    <div class="abs btn hero-btn">CONTACT US</div>
    <a class="abs hero-link">Learn More</a>
  </section>

  <main class="abs content">
    <h2 class="abs section-title" style="left:63px;top:20px">About Corvane Partners</h2>
    <div class="abs photo" style="left:65px;top:47px;width:184px;height:129px" role="img" aria-label="Photo of three colleagues in business attire talking"></div>
    <div class="abs copy" style="left:263px;top:45px">
      <p>Lorem ipsum dolor sit amet, consectetur adipisicing elit, sed do eius-mod tempor incididunt ut labore et dolore magna aliqua. Ut enim ad minim veniam, quis nostrud exercitation ullamco laboris nisi ut ali-quip ex ea commodo consequat.</p>
      <p>Duis aute irure dolor in reprehenderit in voluptate velit esse cillum dolore eu fugiat nulla pariatur. Excepteur sint occaecat cupidatat non proident, sunt in culpa qui officia deserunt mollit anim id est laborum.</p>
    </div>
    <div class="abs rule" style="top:202px"></div>

    <h2 class="abs section-title" style="left:63px;top:222px">Our Approach</h2>
    <div class="abs copy" style="left:66px;top:248px">
      <p>Lorem ipsum dolor sit amet, consectetur adipisicing elit, sed do eius-mod tempor incididunt ut labore et dolore magna aliqua. Ut enim ad minim veniam, quis nostrud exercitation ullamco laboris nisi ut ali-quip ex ea commodo consequat.</p>
      <p>Duis aute irure dolor in reprehenderit in voluptate velit esse cillum dolore eu fugiat nulla pariatur. Excepteur sint occaecat cupidatat non proident, sunt in culpa qui officia deserunt mollit anim id est laborum.</p>
    </div>
    <div class="abs photo" style="left:331px;top:250px;width:185px;height:129px" role="img" aria-label="Photo of an advisor presenting to two clients in a bright office"></div>
    <div class="abs rule" style="top:401px"></div>

    <h2 class="abs section-title" style="left:63px;top:416px">Our Services</h2>
    <div class="abs photo" style="left:65px;top:444px;width:184px;height:128px" role="img" aria-label="Photo of hands reviewing financial charts with pens"></div>
    <div class="abs copy" style="left:263px;top:441px">
      <p>Lorem ipsum dolor sit amet, consectetur adipisicing elit, sed do eius-mod tempor incididunt ut labore et dolore magna aliqua. Ut enim ad minim veniam, quis nostrud exercitation ullamco laboris nisi ut ali-quip ex ea commodo consequat.</p>
      <p>Duis aute irure dolor in reprehenderit in voluptate velit esse cillum dolore eu fugiat nulla pariatur. Excepteur sint occaecat cupidatat non proident, sunt in culpa qui officia deserunt mollit anim id est laborum.</p>
    </div>
  </main>

  <div class="abs rule" style="top:978px"></div>
  <h2 class="abs clients-title">Our Clients</h2>
  <div class="abs client" style="left:80px;font-size:8px"><i></i>Orvix</div>
  <div class="abs client" style="left:138px;font-size:8px">Lumen</div>
  <div class="abs client" style="left:186px;font-size:13px">kelo</div>
  <div class="abs client" style="left:243px">Brisa</div>
  <div class="abs client" style="left:311px;font-size:13px">pixano</div>
  <div class="abs client" style="left:370px;font-size:9px">Quillmark</div>
  <div class="abs client" style="left:450px">Trustel</div>

  <footer class="abs contact">
    <h2 class="abs contact-title">Contact Us</h2>
    <p class="abs contact-note">If you have questions or inquiries, send us through the contact form below.</p>
    <div class="abs field" style="left:63px;top:66px;width:105px;height:16px">Enter your name..</div>
    <div class="abs field" style="left:179px;top:66px;width:106px;height:16px">Enter your email..</div>
    <div class="abs field" style="left:63px;top:90px;width:222px;height:68px">Enter your message..</div>
    <div class="abs btn enquire">ENQUIRE NOW</div>
    <div class="abs details" style="left:297px;top:35px">P: +52 (55) 5550 0148<br>E: info@crvnp.mx</div>
    <div class="abs details" style="left:412px;top:35px">Calle Olmeda 27, Piso 2 Col. Arbolar,<br>CP 06210, México DF, MÉXICO</div>
    <div class="abs map" role="img" aria-label="Street map showing the office location"></div>
    <div class="abs footer-rule"></div>
    <p class="abs copyright">Copyright © 2013 Corvane Partners | Privacy Policy</p>
  </footer>

</div>
</div>
</body>
</html>
```